Business Card for a Wedding Films Business

We require a business card design for our business 'Lewis Marrow Wedding Films'. The logo needs to look classy and high end.

Target Market(s)

Wedding Couples

Contact Information for Business Card

Lewis Marrow Wedding Films
07312 605 227
films@lewismarrowreels.com
www.lewismarrowreels.com

Facebook: @lewismarrowweddingfilms
Instagram: @lewismarrowfilms

Font styles to use
Sans Serif

Requirements
Must have
• Social media icons - Facebook and Instagram

```html
<!DOCTYPE html>
<html lang="en">
<head>
<meta charset="utf-8">
<title>Lewis Marrow Wedding Films — Business Card</title>
<link href="https://fonts.googleapis.com/css2?family=Jost:wght@400;500&family=Montserrat:wght@700&display=swap" rel="stylesheet">
<style>
  :root {
    --page: #9d9e99;
    --card: #ffffff;
    --ink: #2f2f2f;
    --band: #333333;
    --band-text: #ffffff;
    --edge: #d4a72c;
    --photo-light: #f1f0ee;
    --photo-mid: #cfcac4;
    --photo-dark: #3a3a3c;
  }
  * { box-sizing: border-box; margin: 0; padding: 0; }
  html, body { width: 1200px; height: 801px; overflow: hidden; }
  body {
    background: var(--page);
    font-family: "Jost", sans-serif;
    color: var(--ink);
    position: relative;
  }
  .card {
    position: absolute;
    width: 540px;
    height: 310px;
    background: var(--card);
    border-radius: 22px;
    overflow: hidden;
    border-bottom: 3px solid var(--edge);
  }
  .card--front { left: 45px; top: 245px; }
  .card--back { left: 615px; top: 245px; }

  /* front */
  .front-photo {
    position: absolute; right: 0; top: 0; width: 68%; height: 100%;
    background: linear-gradient(90deg, var(--card) 0%, var(--photo-light) 25%, var(--photo-mid) 55%, var(--photo-dark) 100%);
  }
  .front-veil {
    position: absolute; left: 0; bottom: 0; width: 100%; height: 45%;
    background: linear-gradient(180deg, rgba(255,255,255,0) 0%, rgba(244,243,241,0.9) 100%);
  }
  .wordmark { position: absolute; text-align: center; }
  .wordmark__name {
    font-weight: 500; font-size: 26px; letter-spacing: 7px; text-transform: uppercase; white-space: nowrap;
  }
  .wordmark__tag {
    font-weight: 400; font-size: 11px; letter-spacing: 6px; text-transform: uppercase; margin-top: 2px;
  }
  .card--front .wordmark { left: 30px; bottom: 38px; }

  /* back */
  .back-photo {
    position: absolute; left: 0; top: 90px; width: 58%; height: 220px;
    background: radial-gradient(ellipse at 55% 35%, #e7e5e2 0%, #f3f2f0 55%, var(--card) 100%);
  }
  .card--back .wordmark { right: 34px; top: 44px; }
  .card--back .wordmark__name { font-size: 22px; letter-spacing: 6px; }
  .card--back .wordmark__tag { font-size: 10px; }

  .title-band {
    position: absolute; right: 0; top: 166px; width: 300px; height: 30px;
    background: var(--band); display: flex; align-items: center; gap: 10px; padding-left: 16px;
  }
  .title-band__text {
    font-family: "Montserrat", sans-serif; font-weight: 700; font-size: 12.5px;
    letter-spacing: 1px; color: var(--band-text); white-space: nowrap;
  }
  .title-band__mark { width: 12px; height: 12px; background: var(--band-text); flex: none; }

  .contact-list {
    position: absolute; left: 26px; top: 205px; list-style: none;
  }
  .contact-list li {
    display: flex; align-items: center; gap: 7px; font-size: 13.5px; line-height: 19px;
  }
  .contact-list svg { width: 11px; height: 11px; flex: none; }

  .social-band {
    position: absolute; left: 0; bottom: 0; width: 100%; height: 32px;
    background: var(--band); display: flex; align-items: center; justify-content: space-between; padding: 0 26px;
  }
  .social {
    display: flex; align-items: center; gap: 8px; color: var(--band-text); font-size: 12.5px;
  }
  .social__dot { width: 16px; height: 16px; border-radius: 50%; background: var(--band-text); flex: none; }
</style>
</head>
<body>

<section class="card card--front">
  <div class="front-photo" role="img" aria-label="Photograph of a bride and groom embracing under a veil, with a white orchid bouquet"></div>
  <div class="front-veil"></div>
  <div class="wordmark">
    <div class="wordmark__name">Lewis Marrow</div>
    <div class="wordmark__tag">Wedding Films</div>
  </div>
</section>

<section class="card card--back">
  <div class="back-photo" role="img" aria-label="Faded photograph of the wedding couple"></div>
  <div class="wordmark">
    <div class="wordmark__name">Lewis Marrow</div>
    <div class="wordmark__tag">Wedding Films</div>
  </div>

  <div class="title-band">
    <span class="title-band__text">Lewis Marrow Wedding Films</span>
    <span class="title-band__mark"></span>
  </div>

  <ul class="contact-list">
    <li>
      <svg viewBox="0 0 12 12"><circle cx="6" cy="6" r="6" fill="#2f2f2f"/><path d="M4 3.2l1 1-.6.7c.4.9 1 1.5 1.9 1.9l.7-.6 1 1-.7.9C5.1 7.9 3.9 6.6 3.2 4z" fill="#fff"/></svg>
      07312 605 227
    </li>
    <li>
      <svg viewBox="0 0 12 12"><circle cx="6" cy="6" r="6" fill="#2f2f2f"/><rect x="3" y="4" width="6" height="4.2" fill="#fff"/><path d="M3 4l3 2.3L9 4" stroke="#2f2f2f" stroke-width=".7" fill="none"/></svg>
      films@lewismarrowreels.com
    </li>
    <li>
      <svg viewBox="0 0 12 12"><circle cx="6" cy="6" r="6" fill="#2f2f2f"/><circle cx="6" cy="6" r="3" stroke="#fff" stroke-width=".8" fill="none"/><path d="M3 6h6M6 3v6" stroke="#fff" stroke-width=".7"/></svg>
      www.lewismarrowreels.com
    </li>
  </ul>

  <div class="social-band">
    <span class="social"><span class="social__dot"></span>@lewismarrowweddingfilms</span>
    <span class="social"><span class="social__dot"></span>@lewismarrowfilms</span>
  </div>
</section>

</body>
</html>
```